【 概要 】 株式投資の本 電子書籍(lumora)の表紙デザインを募集します。 【 依頼内容 】 ・サイズ: 「2,560 × 1,600 ピクセル」 ・画像ファイルのサイズは 50MB ・タイトル:「月曜の朝に読む、家計簿から始める資産の育て方」 ・著者:森田清二 ・本の帯:下記の文言を1つ入れて帯を作成 (2~3個の組み合わせも可) なぜ株式投資家の9割が負けるのか? 元証券会社社長だから知っている 元証券会社社長が教える 〇〇を見たら負ける? 賢い人は◯◯を捨てる、凡人は〇〇を見る 株式投資初心者が陥りやすい罠とは 株式投資でなぜ損するのか? 【 デザインイメージ 】 ・ターゲット層:投資初心者 40代〜60代 ・雰囲気:思わず手に取りたくなるような、投資を始めたい人に響くイメージ ・色:白ベース (他の配色は自由) ・画像:イラスト・図柄など可、写真は不可 ・縦書き:可 ・文字のレイアウト:自由 注意点・禁止事項 : Lumora セルフ・リリースの表紙画像の要件を満たすようにお願いいたします。 https://help.lumorabooks.example/guide?ref=Q7M3XKP2WZT9LB 【 契約金額(税抜) 】 8000円 ※契約金額(税込)からシステム利用料を差し引いた金額が、ワーカーさまの受取金額となります その他ご質問等ありましたら、気軽にお問い合わせください。 ご応募をお待ちしております! |
こちらの作品が
一番イメージに近かったので採用とさせていただきます。
ご提案いただきありがとうございました。
どれも素晴らしいデザインでした。
また、機会があれば依頼させていただきますので何卒よろしくお願いいたします。

```html
<!DOCTYPE html>
<html lang="ja">
<head>
<meta charset="utf-8">
<title>月曜の朝に読む、家計簿から始める資産の育て方</title>
<link rel="stylesheet" href="https://fonts.googleapis.com/css2?family=Shippori+Mincho+B1:wght@700;800&family=Noto+Sans+JP:wght@500;700;900&family=Cormorant+Garamond:ital,wght@1,500&display=swap">
<style>
  :root {
    --mustard: #b5852f;
    --frame: #5b3714;
    --title-dark: #3a230c;
    --ivory: #ffffff;
    --accent-red: #d3232a;
    --navy: #1f2a44;
    --silhouette: #2b2b2e;
    --paper: #ffffff;
  }
  html, body { margin: 0; padding: 0; overflow: hidden; }
  body { width: 749px; height: 1200px; background: var(--paper); }
  .cover { position: relative; width: 749px; height: 1200px; overflow: hidden; background: var(--paper); }

  .title-panel { position: absolute; left: 0; top: 0; width: 749px; height: 753px; background: var(--mustard); }
  .title-frame { position: absolute; left: 0; top: 0; }

  .title { position: absolute; left: 0; width: 100%; text-align: center; margin: 0;
           font-family: "Shippori Mincho B1", "Noto Serif JP", serif; font-weight: 800; }
  .title-lead { top: 145px; font-size: 44px; color: var(--title-dark); letter-spacing: 2px; }
  .title-main { top: 222px; font-size: 68px; color: var(--ivory); letter-spacing: 2px; }
  .title-tail { top: 320px; font-size: 76px; color: var(--ivory); letter-spacing: 2px; }
  .title-tail .hot { color: var(--accent-red); }

  .author-roman { position: absolute; left: 268px; top: 500px; margin: 0;
                  font-family: "Cormorant Garamond", serif; font-style: italic; font-size: 22px; color: var(--title-dark); }
  .author-name { position: absolute; left: 268px; top: 530px; margin: 0;
                 font-family: "Shippori Mincho B1", serif; font-weight: 700; font-size: 38px; color: var(--title-dark); letter-spacing: 3px; }

  .figure-businessman { position: absolute; left: 40px; top: 610px; width: 105px; height: 320px; }
  .figure-laundry { position: absolute; left: 592px; top: 835px; width: 140px; height: 180px; }

  .obi-badge { position: absolute; left: 181px; top: 764px; width: 440px; height: 54px; border-radius: 6px;
               background: var(--navy); color: #fff; font-family: "Noto Sans JP", sans-serif; font-weight: 700;
               font-size: 28px; line-height: 54px; text-align: center; letter-spacing: 1px; }

  .obi-points { position: absolute; left: 152px; top: 845px; margin: 0; padding: 0; list-style: none;
                font-family: "Noto Sans JP", sans-serif; font-weight: 500; font-size: 28px; line-height: 34px; color: var(--navy); }
  .obi-points li { position: relative; padding-left: 38px; margin-bottom: 22px; }
  .obi-points li::before { content: ""; position: absolute; left: 0; top: 8px; width: 14px; height: 14px;
                           border: 4px solid var(--accent-red); border-radius: 50%; }

  .obi-hook { position: absolute; left: 0; width: 100%; margin: 0; text-align: center;
              font-family: "Noto Sans JP", sans-serif; font-weight: 900; color: var(--accent-red); letter-spacing: 1px; }
  .obi-hook-1 { top: 1030px; font-size: 60px; }
  .obi-hook-2 { top: 1106px; font-size: 60px; }
</style>
</head>
<body>
<main class="cover">
  <section class="title-panel">
    <svg class="title-frame" width="749" height="753" viewBox="0 0 749 753">
      <rect x="34" y="40" width="681" height="436" fill="none" stroke="var(--frame)" stroke-width="4"/>
      <rect x="46" y="52" width="657" height="412" fill="none" stroke="var(--frame)" stroke-width="1.5"/>
    </svg>
    <h1 class="title title-lead">月曜の朝に読む、</h1>
    <p class="title title-main">家計簿から始める</p>
    <p class="title title-tail"><span class="hot">資産</span>の育て方</p>
    <p class="author-roman">Seiji morita</p>
    <p class="author-name">森田清二</p>
  </section>

  <svg class="figure-businessman" role="img" aria-label="鞄を持って立つ会社員のシルエット" viewBox="0 0 105 320" preserveAspectRatio="none">
    <rect width="105" height="320" rx="40" fill="var(--silhouette)"/>
  </svg>
  <svg class="figure-laundry" role="img" aria-label="洗濯物を干す主婦のシルエット" viewBox="0 0 140 180" preserveAspectRatio="none">
    <rect width="140" height="180" rx="36" fill="var(--silhouette)"/>
  </svg>

  <div class="obi-badge">元証券会社社長が教える</div>
  <ul class="obi-points">
    <li>株式投資初心者が<br>陥りやすい罠とは？</li>
    <li>なぜ株式投資家の<br>９割が負けるのか？</li>
  </ul>

  <p class="obi-hook obi-hook-1">賢い人は〇〇を捨てる、</p>
  <p class="obi-hook obi-hook-2">凡人は〇〇を見る</p>
</main>
</body>
</html>
```